~~ Night Club Website ~~

We would like to redo our website for Halo Velvet Room (http://www.halovelvetroom-example.com).

Halo Velvet Room is Edmonton's #1 electronic dance music night club.

We have DJs that fly in from around the world to play at our club and want to be able to properly showcase our upcoming shows and events to increase sales.
Updates

I have now guaranteed the project.  Let's see some brilliant designs!

Target Market(s)

Electronic Dance Music Lovers; College / University Students; Young Professionals

Industry/Entity Type

Electronic

Requirements
Must have
• The site must have the following sections:

1. Home Page
- Rotating Banner where we can put upcoming events
- Chirpline, Socialwall, YouTube, FourSquare buttons
- Our Chirpline feed to automatically post
- Socialwall integration with 'Like' and Comments for upcoming shows
- An email signup section for contests and giveaways that auto-updates the email list in MailChimp
- Streaming music from 9 Pulse Radio

2. Photos
- This needs to integrate right into our Socialwall Albums

3. Weekly Lineup

4. Events
- People need to be able to buy tickets right online via PayPal

5. Bookings
- People need to be able to pick a party package and pay right online via PayPal

6. Contact Us

```html
<!DOCTYPE html>
<html lang="en">
<head>
<meta charset="utf-8">
<title>Halo Velvet Room</title>
<link rel="stylesheet" href="https://fonts.googleapis.com/css2?family=Oswald:wght@400;500;700&family=Open+Sans:wght@400;600&display=swap">
<style>
  :root {
    --bg: #050506;
    --panel: #151517;
    --panel-light: #232326;
    --rule: #2e2e32;
    --text: #8a8a8f;
    --text-dim: #5c5c61;
    --white: #f2f2f2;
    --red: #e3262f;
    --yellow: #f7b51b;
    --orange: #f06a1d;
    --green: #8cc63e;
    --blue: #2f8fd8;
  }
  * { box-sizing: border-box; margin: 0; padding: 0; }
  html, body { width: 820px; height: 1200px; overflow: hidden; }
  body {
    background:
      radial-gradient(circle at 12% 48%, rgba(255,255,255,.05) 0 1px, transparent 2px) 0 0 / 47px 53px,
      radial-gradient(circle at 70% 30%, rgba(255,255,255,.06) 0 1px, transparent 2px) 0 0 / 61px 71px,
      var(--bg);
    font-family: "Open Sans", Arial, sans-serif;
    color: var(--text);
    position: relative;
  }

  /* Header */
  .masthead {
    position: absolute; left: 0; top: 0; width: 820px; height: 200px;
    background:
      radial-gradient(ellipse at 50% 0%, rgba(255,255,255,.55), transparent 30%),
      conic-gradient(from 200deg at 50% 0%, #1b0b3a, #c81b48, #f08a1b, #f4e02a, #3dc23a, #1d9de0, #6a2cd6, #1b0b3a),
      #000;
    -webkit-mask: linear-gradient(#000 70%, transparent);
            mask: linear-gradient(#000 70%, transparent);
  }
  .masthead::after {
    content: ""; position: absolute; inset: 0;
    background: linear-gradient(to bottom, rgba(0,0,0,.1), rgba(0,0,0,.75) 75%);
  }
  .brand {
    position: absolute; left: 0; width: 820px; top: 128px;
    display: flex; justify-content: center; align-items: center; gap: 8px;
    font-family: "Oswald", sans-serif; font-weight: 500; font-size: 17px;
    letter-spacing: 2px; color: var(--white); text-transform: uppercase;
  }
  .brand-mark { width: 14px; height: 14px; background: var(--white); }

  .main-nav {
    position: absolute; left: 95px; top: 196px; width: 646px; height: 24px;
    background: linear-gradient(#2b2b2e, #18181a);
    display: flex; justify-content: space-around; align-items: center;
    font-family: "Oswald", sans-serif; font-size: 11px; letter-spacing: .5px;
    color: var(--white); text-transform: uppercase;
  }

  .banner {
    position: absolute; left: 86px; top: 230px; width: 664px; height: 158px;
    background: var(--panel-light); padding: 7px;
  }
  .banner-photo {
    width: 100%; height: 100%;
    background:
      radial-gradient(ellipse at 30% 10%, rgba(190,120,255,.7), transparent 40%),
      radial-gradient(ellipse at 75% 15%, rgba(120,170,255,.6), transparent 45%),
      linear-gradient(#3a1f5c, #b23a86 60%, #2a1030);
  }

  /* Columns */
  .columns {
    position: absolute; left: 95px; top: 412px; width: 646px; height: 490px;
    display: flex; gap: 22px;
  }
  .col { width: 200px; position: relative; height: 100%; }
  .col-title {
    font-family: "Oswald", sans-serif; font-weight: 500; font-size: 22px;
    letter-spacing: .5px; text-transform: uppercase; color: var(--white);
    margin-bottom: 10px;
  }
  .accent-red { color: var(--red); }
  .accent-yellow { color: var(--yellow); }
  .col-foot {
    position: absolute; left: 0; right: 0; bottom: 0;
    border-top: 1px solid var(--rule); padding-top: 6px;
    font-family: "Oswald", sans-serif; font-size: 13px; letter-spacing: 1px;
    text-transform: uppercase; color: var(--text-dim);
  }
  .welcome-photo {
    height: 98px;
    background:
      radial-gradient(circle at 25% 40%, rgba(255,60,160,.8), transparent 30%),
      radial-gradient(circle at 70% 50%, rgba(60,140,255,.8), transparent 35%),
      #1a0f30;
    margin-bottom: 12px;
  }
  .welcome p { font-size: 8.5px; line-height: 1.55; margin-bottom: 9px; }

  .gallery-grid { display: grid; grid-template-columns: repeat(3, 1fr); gap: 4px; margin-bottom: 6px; }
  .thumb { height: 50px; }
  .t1 { background: linear-gradient(135deg, #5a2a8a, #d73f8b); }
  .t2 { background: linear-gradient(135deg, #1d3c8a, #3fb7e0); }
  .t3 { background: linear-gradient(135deg, #7a1e2e, #f0742a); }
  .t4 { background: linear-gradient(135deg, #2a1a5a, #8a4de0); }
  .t5 { background: linear-gradient(135deg, #0e4a5a, #3fd0a8); }
  .t6 { background: linear-gradient(135deg, #3a1030, #e04a6a); }
  .gallery-label {
    font-family: "Oswald", sans-serif; font-size: 18px; color: var(--white); margin: 4px 0 8px;
  }
  .gallery-date { font-size: 9px; color: var(--yellow); margin-bottom: 4px; }
  .gallery-text { font-size: 8.5px; line-height: 1.55; }
  .gallery-text a { color: var(--white); text-decoration: none; }

  .track-list { list-style: none; }
  .track {
    display: flex; align-items: center; gap: 6px;
    height: 22px; border-bottom: 1px solid var(--rule);
    font-size: 8px; text-transform: uppercase;
  }
  .track-icon { width: 10px; height: 10px; background: var(--red); border-radius: 2px; flex: none; }
  .track-name { color: var(--red); flex: 1; }
  .track-rating { color: var(--red); font-size: 8px; letter-spacing: 1px; }

  /* Lower band */
  .lower {
    position: absolute; left: 88px; top: 928px; width: 662px; height: 232px;
    background: var(--panel); display: flex; gap: 16px; padding: 12px 12px 0;
  }
  .lower-col { width: 200px; }
  .lower-title {
    font-family: "Oswald", sans-serif; font-size: 20px; text-transform: uppercase;
    color: var(--white); line-height: 1.05; margin-bottom: 10px;
  }
  .lower-title.muted { color: #b9b9bd; }
  .like-box { background: #f4f4f4; height: 150px; padding: 8px; color: #333; font-size: 8.5px; }
  .like-head { display: flex; gap: 6px; align-items: center; margin-bottom: 6px; }
  .like-avatar { width: 28px; height: 28px; background: #222; }
  .like-name { font-weight: 600; color: #3b5998; }
  .like-btn { display: inline-block; border: 1px solid #bbb; background: #eee; padding: 0 5px; font-size: 8px; margin-top: 2px; }
  .like-faces { display: grid; grid-template-columns: repeat(5, 1fr); gap: 4px; margin-top: 8px; }
  .like-faces span { height: 26px; background: #c9c9cc; }

  .event { display: flex; gap: 10px; align-items: center; margin-bottom: 14px; }
  .event-date {
    width: 52px; height: 52px; border-radius: 50%; background: var(--green); flex: none;
    display: flex; align-items: center; justify-content: center;
    font-family: "Oswald", sans-serif; font-weight: 700; font-size: 16px; color: var(--white);
  }
  .event-text { font-size: 8.5px; line-height: 1.5; color: #b0b0b4; }

  .contact-label {
    font-family: "Oswald", sans-serif; font-size: 12px; color: var(--blue);
    text-transform: uppercase; margin-top: 8px;
  }
  .contact-value { font-family: "Oswald", sans-serif; font-size: 14px; color: var(--white); letter-spacing: .5px; }
  .contact-value.small { font-size: 11px; }
  .social { display: flex; gap: 6px; justify-content: flex-end; margin-top: 18px; }
  .social span { width: 22px; height: 22px; background: var(--blue); border-radius: 3px; }

  .copyright {
    position: absolute; left: 95px; top: 1172px;
    font-size: 8px; letter-spacing: .5px; color: var(--text-dim); text-transform: uppercase;
  }
</style>
</head>
<body>

<div class="masthead" role="img" aria-label="Dancers in silhouette against colourful club light beams"></div>
<div class="brand"><span class="brand-mark"></span>Halo Velvet Room</div>

<nav class="main-nav">
  <span>Home</span><span>Photos</span><span>Weekly Specials</span><span>Events</span><span>Bookings</span><span>Contact Us</span>
</nav>

<div class="banner">
  <div class="banner-photo" role="img" aria-label="Crowd on a dance floor under purple stage lights"></div>
</div>

<main class="columns">
  <section class="col welcome">
    <h2 class="col-title"><span class="accent-red">Wel</span>come</h2>
    <div class="welcome-photo" role="img" aria-label="Club lights over the dance floor"></div>
    <p>Halo Velvet Room is Edmonton's home for electronic dance music, with guest DJs flown in from around the world every weekend.</p>
    <p>Our staff, lights and sound system turn every night into an event worth remembering. Book a table early and skip the line.</p>
    <p>Check the weekly lineup for specials, themed nights and giveaways, then follow us online to hear about new shows first.</p>
    <div class="col-foot">Read More</div>
  </section>

  <section class="col gallery">
    <h2 class="col-title">Photo <span class="accent-yellow">Gallery</span></h2>
    <div class="gallery-grid">
      <div class="thumb t1" role="img" aria-label="Event photo"></div>
      <div class="thumb t2" role="img" aria-label="Event photo"></div>
      <div class="thumb t3" role="img" aria-label="Event photo"></div>
      <div class="thumb t4" role="img" aria-label="Event photo"></div>
      <div class="thumb t5" role="img" aria-label="Event photo"></div>
      <div class="thumb t6" role="img" aria-label="Event photo"></div>
    </div>
    <div class="gallery-label">Events</div>
    <div class="gallery-date">May 20 12</div>
    <p class="gallery-text">Halo 4th Annual Spin Off: $4 highballs, $4 domestic beers, $99 bottles... <a>See more</a></p>
    <div class="col-foot">View More</div>
  </section>

  <section class="col tracks">
    <h2 class="col-title">DJ <span class="accent-red">Tracks</span></h2>
    <ul class="track-list">
      <li class="track"><span class="track-icon"></span><span class="track-name">Night Drive</span><span class="track-rating">★★★★★</span></li>
      <li class="track"><span class="track-icon"></span><span class="track-name">Low Tide</span><span class="track-rating">★★★★★</span></li>
      <li class="track"><span class="track-icon"></span><span class="track-name">Velvet Pulse</span><span class="track-rating">★★★★★</span></li>
      <li class="track"><span class="track-icon"></span><span class="track-name">Neon Echo</span><span class="track-rating">★★★★★</span></li>
      <li class="track"><span class="track-icon"></span><span class="track-name">Silver Lines</span><span class="track-rating">★★★★★</span></li>
      <li class="track"><span class="track-icon"></span><span class="track-name">Deep Current</span><span class="track-rating">★★★★★</span></li>
      <li class="track"><span class="track-icon"></span><span class="track-name">Halo Rise</span><span class="track-rating">★★★★★</span></li>
      <li class="track"><span class="track-icon"></span><span class="track-name">Glass City</span><span class="track-rating">★★★★★</span></li>
      <li class="track"><span class="track-icon"></span><span class="track-name">After Hours</span><span class="track-rating">★★★★★</span></li>
      <li class="track"><span class="track-icon"></span><span class="track-name">Red Signal</span><span class="track-rating">★★★★★</span></li>
    </ul>
    <div class="col-foot">All Tracks</div>
  </section>
</main>

<section class="lower">
  <div class="lower-col">
    <h3 class="lower-title muted">Find us on Socialwall</h3>
    <div class="like-box">
      <div class="like-head">
        <div class="like-avatar"></div>
        <div><div class="like-name">Halo Velvet Room on Socialwall</div><span class="like-btn">Like</span></div>
      </div>
      <div>1,285 people like Halo Velvet Room</div>
      <div class="like-faces"><span></span><span></span><span></span><span></span><span></span><span></span><span></span><span></span><span></span><span></span></div>
    </div>
  </div>

  <div class="lower-col">
    <h3 class="lower-title">Our Events</h3>
    <div class="event">
      <div class="event-date">30.03</div>
      <p class="event-text">Halo 4th Annual Spin Off 14 Highballs, $4 Domestic Beers, $99 Bottles</p>
    </div>
    <div class="event">
      <div class="event-date">20.04</div>
      <p class="event-text">Halo 4th Annual Spin Off 14 Highballs, $4 Domestic Beers, $99 Bottles</p>
    </div>
  </div>

  <div class="lower-col">
    <h3 class="lower-title muted">For reservations or bottle service</h3>
    <div class="contact-label">Call</div>
    <div class="contact-value">(780) 555-0148</div>
    <div class="contact-label">Email</div>
    <div class="contact-value small">VIP@HALOVELVETROOM-EXAMPLE.COM</div>
    <div class="social"><span aria-label="Chirpline"></span><span aria-label="Socialwall"></span></div>
  </div>
</section>

<footer class="copyright">Copyright © 2012 Halo Velvet Room. All rights reserved.</footer>

</body>
</html>
```